Business card design

I need my logo on this card, things I need the card to have on it
licensed and insured.
owner operators Derek & Milton Halvorsen
my phone number 5418237906
Disaster Recovery, Storm Damage Restoration, Proactive Disaster Plan Management, Roof Repair/Restoration Structural Repair and Reconstruction, Emergency Boarding and Tarping Service, Perimeter Fencing, Emergency Tree Removal,

```html
<!DOCTYPE html>
<html lang="en">
<head>
<meta charset="utf-8">
<title>Halvorsen's Construction – Business Card</title>
<link rel="stylesheet" href="https://fonts.googleapis.com/css2?family=Quicksand:wght@500;600&family=Poppins:wght@600;700&display=swap">
<style>
  :root {
    --blue: #1396e8;
    --blue-dark: #2a7fc6;
    --grey: #717276;
    --ink: #2b2b2d;
    --rule: #9a9a9c;
    --page: #e7e8ea;
    --card: #ffffff;
  }
  * { margin: 0; padding: 0; box-sizing: border-box; }
  html, body { width: 1081px; height: 1200px; overflow: hidden; background: var(--page); }
  body { position: relative; font-family: "Quicksand", sans-serif; }

  .card { position: absolute; left: 151px; width: 778px; height: 445px; background: var(--card); overflow: hidden; }
  .card--front { top: 114px; }
  .card--back { top: 641px; }
  .card__shapes { position: absolute; inset: 0; width: 100%; height: 100%; }
  .abs { position: absolute; white-space: nowrap; }

  .brand { position: absolute; display: flex; flex-direction: column; align-items: center; }
  .brand__mark { display: block; background: var(--blue); }
  .brand__name { color: var(--blue); font-weight: 600; text-align: center; line-height: 1.15; }
  .card--front .brand { left: 104px; top: 46px; width: 242px; }
  .card--front .brand__mark { width: 66px; height: 66px; margin-bottom: 18px; }
  .card--front .brand__name { font-size: 23px; }
  .card--back .brand { left: 566px; top: 34px; width: 176px; }
  .card--back .brand__mark { width: 50px; height: 50px; margin-bottom: 12px; }
  .card--back .brand__name { font-size: 16px; }

  .tagline { left: 101px; top: 313px; color: var(--blue); font-size: 24px; font-weight: 500; }
  .owners { left: 99px; top: 343px; color: var(--ink); font-size: 11.5px; font-weight: 500; }

  .name { left: 469px; top: 165px; font-family: "Poppins", sans-serif; font-weight: 700; font-size: 28px; color: var(--ink); line-height: 1; }
  .name span { color: var(--grey); }
  .designation { left: 469px; top: 200px; font-family: "Poppins", sans-serif; font-weight: 600; font-size: 12.5px; color: var(--grey); }
  .rule { position: absolute; left: 469px; width: 272px; height: 2px; background: var(--rule); }
  .contact { left: 469px; font-family: "Poppins", sans-serif; font-weight: 600; font-size: 13px; color: var(--ink); line-height: 20px; }

  .services-title { left: 86px; top: 84px; color: var(--blue); font-size: 34px; font-weight: 500; }
  .services { position: absolute; left: 86px; top: 126px; list-style: none; color: var(--ink); font-size: 23.5px; font-weight: 500; line-height: 33.5px; }
  .services li { position: relative; padding-left: 19px; white-space: nowrap; }
  .services li::before { content: ""; position: absolute; left: 2px; top: 15px; width: 8px; height: 9px; background: var(--blue);
    clip-path: polygon(50% 0, 100% 25%, 100% 75%, 50% 100%, 0 75%, 0 25%); }
</style>
</head>
<body>

<section class="card card--front" aria-label="Card front">
  <svg class="card__shapes" viewBox="0 0 778 445" aria-hidden="true">
    <polygon points="0,445 211,384 778,445" fill="var(--blue)"/>
    <polygon points="0,256 65,344 0,428" fill="var(--grey)"/>
    <polygon points="16,230 38,209 38,266" fill="var(--blue-dark)"/>
    <polygon points="51,230 77,273 51,301" fill="var(--grey)"/>
    <polygon points="713,24 692,53 713,82" fill="var(--blue-dark)"/>
    <polygon points="726,47 752,93 726,117" fill="var(--grey)"/>
    <g fill="var(--blue)">
      <circle cx="434" cy="185" r="18"/>
      <circle cx="434" cy="275" r="18"/>
      <circle cx="434" cy="327" r="18"/>
      <circle cx="434" cy="381" r="18"/>
    </g>
    <g fill="none" stroke="#fff" stroke-width="1.4" stroke-linecap="round" stroke-linejoin="round">
      <circle cx="434" cy="181" r="4"/>
      <path d="M427 193 q7 -10 14 0"/>
      <path d="M428 268 l3 -1 2 5 -2 2 q2 4 6 6 l2 -2 5 2 -1 3 q-9 1 -15 -15z"/>
      <rect x="427" y="320" width="14" height="10" rx="1"/>
      <path d="M434 330 v3 M430 334 h8"/>
      <path d="M434 390 q-7 -7 -7 -12 a7 7 0 0 1 14 0 q0 5 -7 12z"/>
      <circle cx="434" cy="378" r="2.5"/>
    </g>
  </svg>

  <div class="brand">
    <span class="brand__mark" aria-hidden="true"></span>
    <p class="brand__name">HALVORSEN'S<br>CONSTRUCTION L.L.C</p>
  </div>

  <p class="tagline abs">Licensed and Insured</p>
  <p class="owners abs">Owner operators Derek &amp; Milton Halvorsen</p>

  <p class="name abs">YOUR <span>NAME</span></p>
  <p class="designation abs">DESIGNATION</p>
  <div class="rule" style="top:222px"></div>
  <p class="contact abs" style="top:265px">541-823-7906</p>
  <div class="rule" style="top:292px"></div>
  <p class="contact abs" style="top:302px">info@halvorsenbuild.com<br>www.halvorsenbuild.com</p>
  <div class="rule" style="top:351px"></div>
  <p class="contact abs" style="top:362px">your Address&nbsp; 2223, Absd, Street,<br>Country, Ak 9951</p>
</section>

<section class="card card--back" aria-label="Card back">
  <svg class="card__shapes" viewBox="0 0 778 445" aria-hidden="true">
    <polygon points="0,445 567,384 778,445" fill="var(--blue)"/>
    <polygon points="50,47 25,89 50,116" fill="var(--grey)"/>
    <polygon points="64,24 86,50 64,82" fill="var(--blue-dark)"/>
    <polygon points="726,232 701,275 726,301" fill="var(--grey)"/>
    <polygon points="740,209 761,236 740,266" fill="var(--blue-dark)"/>
    <polygon points="778,256 713,345 778,426" fill="var(--grey)"/>
  </svg>

  <div class="brand">
    <span class="brand__mark" aria-hidden="true"></span>
    <p class="brand__name">HALVORSEN'S<br>CONSTRUCTION L.L.C</p>
  </div>

  <h2 class="services-title abs">Our Services</h2>
  <ul class="services">
    <li>Disaster Recovery</li>
    <li>Storm Damage Restoration</li>
    <li>Proactive Disaster Plan Management</li>
    <li>Roof Repair/Restoration Structural<br>Repair and Reconstruction,</li>
    <li>Emergency Boarding and Tarping Service</li>
    <li>Perimeter Fencing</li>
    <li>Emergency Tree Removal</li>
  </ul>
</section>

</body>
</html>
```